Flyer Design Project

Something bold, something creative, something colorful. Will have 3 full time employees passing these out to business owners locally as well as national conventions.
Need something that will grab attention and remain a reminder, before they end up hitting the trash can...
Site can be found at www.QuillOrbitPress.example
A few different logo formats are attached.
2 sizes would be nice. 8.5" x 11" and 4"x6 (they can look the same)
No specifics on graphics, colors or info. Stay somewhat consistent with the website. I basically just want people to know we are here and we are definitely the cheapest print prices in the nation.
Target Market(s)
Anyone that needs print work done.
Industry/Entity Type
Business
Look and feel

```html
<!DOCTYPE html>
<html lang="en">
<head>
<meta charset="utf-8">
<title>Quill Orbit Press — Flyer</title>
<link rel="stylesheet" href="https://fonts.googleapis.com/css2?family=Open+Sans:wght@400;800&display=swap">
<style>
  :root {
    --backdrop: #173a6b;
    --panel: rgba(14, 18, 22, 0.92);
    --ink-light: #ffffff;
    --accent-teal: #3fb9b0;
    --tone-orange: #f08a2a;
    --tone-yellow: #e9dd2c;
    --tone-teal: #1fb3a8;
    --tone-magenta: #d8267a;
    --tone-violet: #6a3fb0;
  }
  * { box-sizing: border-box; margin: 0; padding: 0; }
  html, body {
    width: 1200px;
    height: 817px;
    overflow: hidden;
    background: var(--backdrop);
    font-family: "Open Sans", Arial, sans-serif;
  }
  .canvas {
    position: relative;
    width: 1200px;
    height: 817px;
  }
  .flyer {
    position: absolute;
    left: 330px;
    top: 42px;
    width: 540px;
    height: 732px;
    overflow: hidden;
    box-shadow: 0 10px 30px rgba(0, 0, 0, 0.45);
  }
  .flyer__photo {
    position: absolute;
    inset: 0;
    background:
      radial-gradient(ellipse at 20% 85%, var(--tone-orange) 0%, transparent 35%),
      radial-gradient(ellipse at 95% 40%, var(--tone-violet) 0%, transparent 30%),
      radial-gradient(ellipse at 85% 10%, var(--tone-magenta) 0%, transparent 35%),
      radial-gradient(ellipse at 40% 60%, var(--tone-teal) 0%, transparent 45%),
      linear-gradient(170deg, var(--tone-orange) 0%, var(--tone-yellow) 30%, var(--tone-yellow) 45%, var(--tone-teal) 70%, var(--tone-orange) 100%);
  }
  .offer-panel {
    position: absolute;
    left: 268px;
    top: 268px;
    width: 256px;
    height: 432px;
    background: var(--panel);
    color: var(--ink-light);
    text-align: center;
    padding: 24px 12px 0;
    display: flex;
    flex-direction: column;
    align-items: center;
  }
  .offer-panel__brand {
    font-weight: 800;
    font-size: 20px;
    line-height: 1.15;
    color: var(--ink-light);
    height: 96px;
    display: flex;
    align-items: center;
    justify-content: center;
    gap: 10px;
  }
  .offer-panel__brand-dot {
    width: 14px;
    height: 14px;
    border-radius: 50%;
    background: var(--accent-teal);
    flex: none;
  }
  .headline {
    font-weight: 800;
    text-transform: uppercase;
    letter-spacing: -0.5px;
    margin-top: 22px;
  }
  .headline__line { display: block; }
  .headline__line--nobody { font-size: 44px; line-height: 46px; }
  .headline__line--beats { font-size: 56px; line-height: 58px; }
  .headline__line--our-print { font-size: 37px; line-height: 44px; }
  .headline__line--prices { font-size: 53px; line-height: 56px; }
  .guarantee {
    font-weight: 800;
    font-size: 17px;
    line-height: 22px;
    text-transform: uppercase;
    margin-top: 6px;
  }
  .website {
    font-weight: 400;
    font-size: 17px;
    line-height: 24px;
    color: var(--accent-teal);
    margin-top: 12px;
  }
</style>
</head>
<body>
<main class="canvas">
  <article class="flyer">
    <div class="flyer__photo" role="img" aria-label="Close-up photograph of face paint in bright yellow, teal, orange and magenta powder"></div>
    <section class="offer-panel">
      <div class="offer-panel__brand">
        <span class="offer-panel__brand-dot"></span>
        <span>Quill Orbit Press</span>
      </div>
      <h1 class="headline">
        <span class="headline__line headline__line--nobody">Nobody</span>
        <span class="headline__line headline__line--beats">Beats</span>
        <span class="headline__line headline__line--our-print">Our Print</span>
        <span class="headline__line headline__line--prices">Prices!</span>
      </h1>
      <p class="guarantee">100% Guaranteed</p>
      <p class="website">QuillOrbitPress.example</p>
    </section>
  </article>
</main>
</body>
</html>
```